Brand Business Card for Hotel Cloud Management System

Hello designers,
we are looking for a new brand business card for our product Stayvora. Our brand Stayvora is a hotel management system for small hotels, B&B, guesthouses etc. and just recently we are expanding our offer to other European markets. Therefore we need a business card that will communicate not only to the end-users (hoteliers) but also to potential business partners/ We would like the brand business card to be professional looking, but not too serius, modern, elegant, clean, Our brand color is orange, dark grey and it would be nice to see both combined.

Please visit our website www.stayvora.eu to get more impression on what our brand stayvora stands for.

Please find attached stayvora logo.

Target Market(s)

small hotels, hoteliers, B&B owners, potential business partners

Industry/Entity Type

Software Service

Contact Information for Business Card

Stayvora
- hotel software solutions - web booking engine - multi channel manager
www.stayvora.eu
T: +38614738265
E: info@stayvora.net

Font styles to use
Serif
Sans Serif

Colors
f37122
aaaaaa
606060
f6f6f6

Requirements
Must have
• Logo of the brand
• the layout of the business card should be in connection with the look and feel of the website stayvora.eu and logo stayvora;

```html
<!DOCTYPE html>
<html lang="en">
<head>
<meta charset="utf-8">
<title>Stayvora Business Card</title>
<link rel="stylesheet" href="https://fonts.googleapis.com/css2?family=Quicksand:wght@400;500;700&display=swap">
<style>
  :root {
    --brand-orange: #f37122;
    --card-black: #151515;
    --stage-grey: #6b6b6d;
    --text-white: #f6f6f6;
    --text-soft: #aaaaaa;
  }
  * { margin: 0; padding: 0; box-sizing: border-box; }
  html, body {
    width: 1200px;
    height: 913px;
    overflow: hidden;
  }
  body {
    background: var(--stage-grey);
    font-family: "Quicksand", "Helvetica Neue", Arial, sans-serif;
    display: flex;
    align-items: center;
    justify-content: center;
  }
  .business-card {
    width: 470px;
    height: 820px;
    background: var(--card-black);
    border-radius: 4px;
    box-shadow: 0 18px 40px rgba(0, 0, 0, 0.35);
    color: var(--text-white);
    display: flex;
    flex-direction: column;
    align-items: center;
    padding-top: 150px;
    text-align: center;
  }
  .brand-mark {
    display: flex;
    flex-direction: column;
    align-items: center;
  }
  .brand-square {
    width: 74px;
    height: 74px;
    background: var(--brand-orange);
    border-radius: 6px;
    margin-bottom: 22px;
  }
  .brand-name {
    font-size: 68px;
    font-weight: 700;
    letter-spacing: 0.5px;
    line-height: 1;
    color: var(--text-white);
  }
  .brand-tagline {
    font-size: 21px;
    font-weight: 400;
    letter-spacing: 1.5px;
    color: var(--text-white);
    margin-top: 8px;
  }
  .divider {
    width: 32px;
    height: 3px;
    background: var(--brand-orange);
    margin: 40px auto;
  }
  .services {
    list-style: none;
    font-size: 19px;
    font-weight: 700;
    line-height: 1.5;
    letter-spacing: 0.5px;
  }
  .contact {
    font-size: 19px;
    font-weight: 400;
    line-height: 1.55;
    letter-spacing: 0.5px;
    color: var(--text-white);
  }
  .contact-label {
    color: var(--brand-orange);
    font-weight: 700;
    margin-right: 4px;
  }
</style>
</head>
<body>
  <article class="business-card">
    <header class="brand-mark">
      <div class="brand-square" aria-hidden="true"></div>
      <h1 class="brand-name">Stayvora</h1>
      <p class="brand-tagline">hotel pms service</p>
    </header>

    <div class="divider" aria-hidden="true"></div>

    <ul class="services">
      <li>hotel software solutions</li>
      <li>web booking engine</li>
      <li>multi channel manager</li>
    </ul>

    <div class="divider" aria-hidden="true"></div>

    <address class="contact" style="font-style: normal;">
      <div><span class="contact-label">W:</span>www.stayvora.eu</div>
      <div><span class="contact-label">T:</span>+38614738265</div>
      <div><span class="contact-label">E:</span>info@stayvora.net</div>
    </address>
  </article>
</body>
</html>
```